ko7ara card

the business is a virtual space for showcasing art, libraries, science, food and gifts

high end - new look - nothing fussy - clean lines - bit of colour

needs to last for ten years - at least

think the number 11 in yellow with a purple background

hope that is enough of a brief - smile

Target Market(s)

all ages

Industry/Entity Type

Business

Contact Information for Business Card

ko7ara.com
tam corley = caretaker
virtual space & harlow WA > australia

Requirements
Must have
• happy for you to choose
Nice to have
• ditto
Should not have
• anything boring - something that appeals to Gen I

```html
<!DOCTYPE html>
<html lang="en">
<head>
<meta charset="utf-8">
<title>ko7ara card</title>
<link rel="stylesheet" href="https://fonts.googleapis.com/css2?family=Saira:wght@300;400;700&display=swap">
<style>
  :root {
    --canvas-bg: #ebe8ee;
    --card-white: #f4f4f7;
    --brand-purple: #7b3590;
    --brand-yellow: #e2c400;
    --wordmark-light: #ece2f1;
    --ink: #141414;
    --ink-soft: #3a3a3a;
    --card-shadow: 0 18px 40px rgba(40, 20, 50, 0.18);
  }
  * { box-sizing: border-box; margin: 0; padding: 0; }
  html, body {
    width: 1200px;
    height: 1000px;
    overflow: hidden;
  }
  body {
    background: var(--canvas-bg);
    font-family: "Saira", sans-serif;
    display: flex;
    align-items: center;
    justify-content: center;
    gap: 60px;
  }
  .card {
    width: 525px;
    height: 300px;
    border-radius: 4px;
    box-shadow: var(--card-shadow);
    position: relative;
    overflow: hidden;
  }

  /* Contact side */
  .card--contact { background: var(--card-white); }
  .brand-block {
    position: absolute;
    top: 34px;
    right: 40px;
    display: flex;
    flex-direction: column;
    align-items: flex-end;
    gap: 8px;
  }
  .brand-square {
    width: 62px;
    height: 62px;
    background: var(--brand-purple);
  }
  .brand-name {
    font-size: 30px;
    font-weight: 400;
    color: var(--ink);
    line-height: 1;
    letter-spacing: 0.2px;
  }
  .contact-details {
    position: absolute;
    left: 40px;
    bottom: 40px;
    line-height: 1.25;
  }
  .contact-name {
    font-size: 19px;
    font-weight: 700;
    color: var(--ink);
  }
  .contact-line {
    font-size: 18px;
    font-weight: 300;
    color: var(--ink-soft);
  }

  /* Brand side */
  .card--brand {
    background: var(--brand-purple);
    display: flex;
    align-items: center;
    justify-content: center;
    gap: 16px;
  }
  .brand-accent {
    width: 34px;
    height: 34px;
    background: var(--brand-yellow);
  }
  .brand-wordmark {
    font-size: 66px;
    font-weight: 400;
    color: var(--wordmark-light);
    line-height: 1;
    letter-spacing: 0.5px;
  }
</style>
</head>
<body>
  <section class="card card--contact" aria-label="Contact side">
    <div class="brand-block">
      <div class="brand-square"></div>
      <div class="brand-name">ko7ara.com</div>
    </div>
    <div class="contact-details">
      <p class="contact-name">Tam Corley</p>
      <p class="contact-line">caretaker virtual space</p>
      <p class="contact-line">harlow WA</p>
    </div>
  </section>

  <section class="card card--brand" aria-label="Brand side">
    <div class="brand-accent"></div>
    <div class="brand-wordmark">ko7ara.com</div>
  </section>
</body>
</html>
```